Business Card Design

Recruitment Company. Want to keep the logo and the green colour

Industry/Entity Type

Business

Contact Information for Business Card

Hi,

1.)
MARTIN COLLARD
Director
Level 4, 238 Finch Terrace
Brisbane QLD 4000
M 0412 604 337
E martin@paceltalent.com.au
www.paceltalent.com.au

2.)
TOM WHITFORD
Director
Level 4, 238 Finch Terrace
Brisbane QLD 4000
M 0419 572 641
E tom@paceltalent.com.au

Want something different and eye catching, happy for you guys to use your design flare to work some magic with these.

Many Thanks
Tom

```html
<!DOCTYPE html>
<html lang="en">
<head>
<meta charset="utf-8">
<title>Pacel Talent – Business Cards</title>
<link href="https://fonts.googleapis.com/css2?family=Open+Sans:wght@400;600;700;800&display=swap" rel="stylesheet">
<style>
  :root {
    --page-bg: #ededeb;
    --card-white: #ffffff;
    --divider-grey: #e4e6e4;
    --green-deep: #27b556;
    --green-mid: #4cc24a;
    --green-light: #93d94a;
    --brand-green: #3aa83c;
    --text-dark: #1d3b22;
    --text-white: #ffffff;
    --shadow: rgba(40, 50, 40, 0.18);
  }
  * { box-sizing: border-box; margin: 0; padding: 0; }
  html, body {
    width: 1200px; height: 856px; overflow: hidden;
    background: var(--page-bg);
    font-family: "Open Sans", Arial, sans-serif;
  }
  .card-set {
    position: absolute; inset: 0;
    display: flex; flex-direction: column;
    align-items: center; justify-content: center; gap: 40px;
  }
  .business-card {
    position: relative;
    width: 620px; height: 378px;
    border-radius: 30px; overflow: hidden;
    background: var(--card-white);
    box-shadow: 0 8px 24px var(--shadow);
    display: flex;
  }
  .brand-panel {
    width: 348px; height: 100%;
    display: flex; align-items: center; justify-content: center; gap: 12px;
  }
  .brand-dot {
    width: 26px; height: 26px; border-radius: 50%;
    background: var(--brand-green);
  }
  .brand-name {
    font-weight: 800; font-size: 38px; letter-spacing: -0.5px;
    color: var(--brand-green);
  }
  .panel-divider {
    width: 14px; height: 100%;
    background: var(--divider-grey);
  }
  .contact-panel {
    flex: 1; height: 100%;
    background: linear-gradient(135deg, var(--green-deep) 0%, var(--green-mid) 50%, var(--green-light) 100%);
    padding: 98px 0 0 34px;
    color: var(--text-white);
  }
  .person-name { font-weight: 700; font-size: 17px; letter-spacing: 0.2px; }
  .person-role { font-weight: 400; font-size: 14px; margin-bottom: 16px; }
  .office-address {
    font-weight: 700; font-size: 13.5px; line-height: 1.35;
    color: var(--text-dark); text-transform: uppercase;
    margin-bottom: 4px;
  }
  .contact-line {
    display: flex; align-items: center; gap: 7px;
    font-size: 13.5px; line-height: 1.45;
  }
  .contact-icon {
    width: 12px; height: 12px; flex: none;
    background: var(--text-white); border-radius: 2px;
    display: flex; align-items: center; justify-content: center;
  }
  .contact-icon svg { width: 9px; height: 9px; }
</style>
</head>
<body>
<main class="card-set">

  <article class="business-card">
    <div class="brand-panel">
      <span class="brand-dot"></span>
      <span class="brand-name">Pacel Talent</span>
    </div>
    <div class="panel-divider"></div>
    <div class="contact-panel">
      <p class="person-name">MARTIN COLLARD</p>
      <p class="person-role">Director</p>
      <p class="office-address">Level 4,<br>238 Finch Terrace<br>Brisbane QLD 4000</p>
      <p class="contact-line"><span class="contact-icon"><svg viewBox="0 0 10 10"><path d="M2 1h2l1 2-1 1a5 5 0 0 0 2 2l1-1 2 1v2c-4 0-7-3-7-7z" fill="#3aa83c"/></svg></span>0412 604 337</p>
      <p class="contact-line"><span class="contact-icon"><svg viewBox="0 0 10 10"><rect x="1" y="2.5" width="8" height="5" fill="none" stroke="#3aa83c"/><path d="M1 2.5l4 3 4-3" fill="none" stroke="#3aa83c"/></svg></span>martin@paceltalent.com.au</p>
      <p class="contact-line"><span class="contact-icon"><svg viewBox="0 0 10 10"><circle cx="5" cy="5" r="3.6" fill="none" stroke="#3aa83c"/><path d="M1.4 5h7.2M5 1.4v7.2" stroke="#3aa83c" stroke-width="0.8"/></svg></span>www.paceltalent.com.au</p>
    </div>
  </article>

  <article class="business-card">
    <div class="brand-panel">
      <span class="brand-dot"></span>
      <span class="brand-name">Pacel Talent</span>
    </div>
    <div class="panel-divider"></div>
    <div class="contact-panel">
      <p class="person-name">TOM WHITFORD</p>
      <p class="person-role">Director</p>
      <p class="office-address">Level 4,<br>238 Finch Terrace<br>Brisbane QLD 4000</p>
      <p class="contact-line"><span class="contact-icon"><svg viewBox="0 0 10 10"><path d="M2 1h2l1 2-1 1a5 5 0 0 0 2 2l1-1 2 1v2c-4 0-7-3-7-7z" fill="#3aa83c"/></svg></span>0419 572 641</p>
      <p class="contact-line"><span class="contact-icon"><svg viewBox="0 0 10 10"><rect x="1" y="2.5" width="8" height="5" fill="none" stroke="#3aa83c"/><path d="M1 2.5l4 3 4-3" fill="none" stroke="#3aa83c"/></svg></span>tom@paceltalent.com.au</p>
      <p class="contact-line"><span class="contact-icon"><svg viewBox="0 0 10 10"><circle cx="5" cy="5" r="3.6" fill="none" stroke="#3aa83c"/><path d="M1.4 5h7.2M5 1.4v7.2" stroke="#3aa83c" stroke-width="0.8"/></svg></span>www.paceltalent.com.au</p>
    </div>
  </article>

</main>
</body>
</html>
```